Kestrel Hollow Brewing Company New Website with Food Ordering

We need a wordpress-based website for a local brewery & pizza kitchen. The final design will have 6 primary pages: home page, order pizza, our beers, visit us, about us, merch store. The website must integrate with tallyplate for kitchens for online ordering for takeout and delivery. It will also a feature a selection of beers and help customers navigate to the brewery and find hours of operation. The existing website is kestrelhollowbrew.com. This is a very old website.

Industry/Entity Type

Brewery and food service

Coding

Coded - Design and coding required

Number of Pages Required

5+ page

Font styles to use
Sans Serif

Requirements
Must have
• ability to integrate seamlessly with tallyplate for kitchens, 21+ age gate
Nice to have
• see attached pdf

```html
<!DOCTYPE html>
<html lang="en">
<head>
<meta charset="utf-8">
<title>Kestrel Hollow Brewing Company</title>
<link href="https://fonts.googleapis.com/css2?family=Libre+Caslon+Text:ital,wght@0,400;0,700;1,700&family=Roboto:wght@300;400;500;700&display=swap" rel="stylesheet">
<style>
  :root {
    --red: #c8102e;
    --red-deep: #a90d27;
    --ink: #231f20;
    --paper: #faf6f4;
    --white: #ffffff;
    --muted: #4a4446;
    --serif: "Libre Caslon Text", Georgia, serif;
    --sans: "Roboto", Arial, sans-serif;
  }
  * { box-sizing: border-box; margin: 0; padding: 0; }
  html, body { width: 851px; height: 1200px; overflow: hidden; }
  body { position: relative; background: var(--paper); font-family: var(--sans); color: var(--ink); }
  .abs { position: absolute; }

  /* top notice bar */
  .notice-bar { left: 0; top: 0; width: 851px; height: 26px; background: var(--red); color: var(--white); }
  .notice-bar .notice { position: absolute; left: 185px; top: 8px; font-size: 7.4px; font-weight: 300; white-space: nowrap; display: flex; align-items: center; gap: 4px; }
  .notice b { font-weight: 500; }
  .social-dots { position: absolute; left: 679px; top: 5px; display: flex; gap: 5px; }
  .social-dots span { width: 16px; height: 16px; border: 1px solid var(--white); border-radius: 50%; }

  /* header */
  .brand { left: 93px; top: 32px; display: flex; align-items: center; gap: 6px; }
  .brand .mark { width: 14px; height: 14px; background: var(--red); flex: none; }
  .brand .name { font-family: var(--serif); font-weight: 700; font-size: 10.5px; line-height: 1.2; color: var(--red); }
  .main-nav { left: 353px; top: 40px; display: flex; gap: 20px; font-size: 8px; font-weight: 500; color: var(--ink); }
  .btn-order { left: 658px; top: 32px; width: 100px; height: 26px; background: var(--red); color: var(--white); border-radius: 3px; font-family: var(--serif); font-weight: 700; font-size: 8.6px; letter-spacing: .4px; display: flex; align-items: center; justify-content: center; }

  /* hero */
  .hero-frame { left: 0; top: 0; }
  .hero-title { left: 40px; top: 186px; width: 360px; text-align: center; color: var(--white); font-family: var(--serif); font-weight: 700; font-size: 30.5px; line-height: 42px; letter-spacing: .6px; }
  .hero-actions { left: 85px; top: 334px; display: grid; grid-template-columns: 128px 128px; gap: 11px 11px; }
  .hero-actions a { height: 32px; border: 1.5px solid var(--white); border-radius: 3px; color: var(--white); font-family: var(--serif); font-weight: 700; font-size: 10.5px; letter-spacing: .8px; display: flex; align-items: center; justify-content: center; text-decoration: none; }
  .hero-actions a.primary { background: var(--white); color: var(--red); }
  .slider-dots { left: 400px; top: 493px; display: flex; gap: 7px; }
  .slider-dots span { width: 6px; height: 6px; border: 1px solid var(--white); border-radius: 50%; }
  .slider-dots span.on { background: var(--white); }
  .ribbon-text { left: 744px; top: 106px; width: 70px; text-align: center; color: var(--white); font-family: var(--serif); font-style: italic; font-weight: 700; font-size: 13.5px; line-height: 20px; }

  /* detroit pizza section */
  .pizza-frame { left: 84px; top: 588px; width: 330px; height: 277px; border: 1.5px solid var(--red); border-radius: 8px; }
  .pizza-photo { left: 90px; top: 595px; width: 332px; height: 263px; border-radius: 6px; background: linear-gradient(135deg, #8a2418 0%, #c24a2a 35%, #e8c27a 55%, #a8321e 75%, #6b1a12 100%); box-shadow: 0 3px 8px rgba(0,0,0,.25); }
  .intro-title { left: 444px; top: 605px; font-family: var(--serif); font-weight: 700; font-size: 21.5px; color: var(--ink); white-space: nowrap; }
  .intro-title em { font-style: normal; color: var(--red); }
  .intro-rule { left: 444px; top: 638px; width: 47px; height: 2px; background: var(--red); }
  .intro-copy { left: 444px; top: 650px; width: 324px; font-size: 8.3px; font-weight: 300; line-height: 15.5px; text-align: justify; color: var(--muted); }
  .btn-menu { left: 444px; top: 816px; width: 100px; height: 25px; background: var(--red); color: var(--white); border-radius: 3px; font-family: var(--serif); font-weight: 700; font-size: 8.6px; letter-spacing: .5px; display: flex; align-items: center; justify-content: center; }

  /* footer */
  .footer-bg { left: 0; top: 900px; }
  .footer-brand { left: 120px; top: 1030px; display: flex; align-items: center; gap: 8px; }
  .footer-brand .mark { width: 26px; height: 26px; background: var(--red); }
  .footer-brand .name { font-family: var(--serif); font-weight: 700; font-size: 17px; line-height: 1.2; color: var(--white); }
  .foot-col { top: 1003px; color: var(--white); }
  .foot-col h3 { font-family: var(--serif); font-weight: 700; font-size: 10.6px; letter-spacing: .5px; margin-bottom: 7px; }
  .foot-col ul { list-style: none; }
  .foot-col li { font-size: 8.5px; font-weight: 300; height: 15.5px; display: flex; align-items: center; gap: 9px; }
  .foot-col li svg { flex: none; }
  .contact li { align-items: flex-start; height: auto; margin-bottom: 10px; line-height: 15.5px; }
  .contact li svg { margin-top: 3px; }
  .dot { width: 8px; height: 8px; border-radius: 50%; background: var(--white); flex: none; }
  .cards { display: flex; gap: 4px; margin-left: 1px; }
  .cards span { width: 26px; height: 17px; border-radius: 2px; background: #d9d4d5; }
  .foot-rule { left: 79px; top: 1148px; width: 693px; height: 1px; background: #5a5455; }
  .copyright { left: 0; top: 1161px; width: 851px; text-align: center; font-size: 7.8px; font-weight: 300; color: var(--white); }
</style>
</head>
<body>

  <div class="abs notice-bar">
    <div class="notice">
      <svg width="8" height="8" viewBox="0 0 10 10"><circle cx="5" cy="5" r="4" fill="none" stroke="#fff" stroke-width="1.1"/><path d="M5 2.6V5l1.6 1" fill="none" stroke="#fff" stroke-width="1.1"/></svg>
      <span>The Kitchen is open <b>Thursday-Monday.</b> Kitchen stops taking orders <b>45 minutes before</b> the bar closes. Last call is <b>15 minutes before</b> close.</span>
    </div>
    <div class="social-dots"><span></span><span></span><span></span><span></span></div>
  </div>

  <div class="abs brand">
    <span class="mark"></span>
    <span class="name">Kestrel Hollow<br>Brewing Co.</span>
  </div>

  <nav class="abs main-nav">
    <span>THE KITCHEN</span><span>OUR BEERS</span><span>VISIT US</span><span>ABOUT US</span><span>MERCH</span>
  </nav>
  <div class="abs btn-order">ORDER ONLINE</div>

  <svg class="abs hero-frame" width="851" height="560" viewBox="0 0 851 560">
    <defs>
      <radialGradient id="heroShade" cx="0.5" cy="0.5" r="0.7">
        <stop offset="0" stop-color="#d01a36" stop-opacity="0"/>
        <stop offset="1" stop-color="#8e0b22" stop-opacity=".45"/>
      </radialGradient>
      <linearGradient id="beerPizza" x1="0" y1="0" x2="0" y2="1">
        <stop offset="0" stop-color="#7d8f6a"/>
        <stop offset=".45" stop-color="#b9bcbd"/>
        <stop offset=".7" stop-color="#b4472d"/>
        <stop offset="1" stop-color="#d9b062"/>
      </linearGradient>
    </defs>
    <polygon points="0,114 425,61 851,114 851,487 425,546 0,487" fill="#231f20"/>
    <polygon points="11,127 425,90 425,518 11,472" fill="#c8102e"/>
    <polygon points="11,127 425,90 425,518 11,472" fill="url(#heroShade)"/>
    <polygon points="425,90 840,128 840,474 425,518" fill="url(#beerPizza)" role="img" aria-label="Photo of two pale ale cans behind a pepperoni and banana pepper square pizza on an outdoor patio table"/>
    <polygon points="744,94 815,94 815,177 779,160 744,177" fill="#c8102e"/>
    <polygon points="815,94 822,110 815,110" fill="#8e0b22"/>
    <polygon points="749,100 810,100 810,170 779,156 749,170" fill="none" stroke="#fff" stroke-width=".8" stroke-dasharray="3 2"/>
  </svg>

  <div class="abs ribbon-text">Try<br>Tangy!</div>

  <h1 class="abs hero-title">SQUARE PIZZA<br>AND GREAT BEER IN<br>PORTLAND, MAINE</h1>
  <div class="abs hero-actions">
    <a class="primary">ORDER PIZZA</a><a>VISIT US</a>
    <a>OUR BEERS</a><a>ABOUT US</a>
  </div>
  <div class="abs slider-dots"><span></span><span class="on"></span><span></span><span></span></div>

  <div class="abs pizza-frame"></div>
  <div class="abs pizza-photo" role="img" aria-label="Photo of a Detroit-style square pizza with cupped pepperoni, green onion and grated cheese on a cooling rack"></div>

  <h2 class="abs intro-title">What is Detroit<em>-style pizza?</em></h2>
  <div class="abs intro-rule"></div>
  <p class="abs intro-copy">Lorem ipsum dolor sit amet, consectetur adipiscing elit, sed do eiusmod tempor incididunt ut labore et dolore magna aliqua. Quis ipsum suspendisse ultrices gravida. Risus commodo viverra maecenas accumsan lacus vel facilisis. perspiciatis unde omnis iste natus error sit voluptatem accusantium doloremque laudantium, totam rem aperiam, eaque ipsa quae ab illo inventore veritatis et quasi architecto beatae vitae dicta sunt explicabo. Nemo enim ipsam voluptatem quia voluptas sit aspernatur aut odit aut fugit, sed quia consequuntur magni dolores eos qui ratione voluptatem sequi nesciunt. Neque porro quisquam est, qui dolorem ipsum quia dolor sit amet, consectetur, adipisci velit, sed quia non numquam eius modi tempora incidunt ut labore et dolore magnam aliquam quaerat voluptatem. Ut enim ad minima veniam quis nostrum exercitationem.</p>
  <div class="abs btn-menu">VIEW FULL MENU</div>

  <svg class="abs footer-bg" width="851" height="300" viewBox="0 0 851 300">
    <polygon points="0,62 425,13 851,62 851,300 0,300" fill="#c8102e"/>
    <polygon points="0,71 425,30 851,71 851,300 0,300" fill="#231f20"/>
  </svg>

  <div class="abs footer-brand">
    <span class="mark"></span>
    <span class="name">Kestrel Hollow<br>Brewing Co.</span>
  </div>

  <div class="abs foot-col" style="left:321px">
    <h3>QUICK LINKS</h3>
    <ul>
      <li><svg width="6" height="6" viewBox="0 0 6 6"><path d="M.5 .5 2.8 3 .5 5.5M3.2 .5 5.5 3 3.2 5.5" fill="none" stroke="#fff" stroke-width="1"/></svg>The Kitchen</li>
      <li><svg width="6" height="6" viewBox="0 0 6 6"><path d="M.5 .5 2.8 3 .5 5.5M3.2 .5 5.5 3 3.2 5.5" fill="none" stroke="#fff" stroke-width="1"/></svg>Our Beers</li>
      <li><svg width="6" height="6" viewBox="0 0 6 6"><path d="M.5 .5 2.8 3 .5 5.5M3.2 .5 5.5 3 3.2 5.5" fill="none" stroke="#fff" stroke-width="1"/></svg>Visit Us</li>
      <li><svg width="6" height="6" viewBox="0 0 6 6"><path d="M.5 .5 2.8 3 .5 5.5M3.2 .5 5.5 3 3.2 5.5" fill="none" stroke="#fff" stroke-width="1"/></svg>About Us</li>
      <li><svg width="6" height="6" viewBox="0 0 6 6"><path d="M.5 .5 2.8 3 .5 5.5M3.2 .5 5.5 3 3.2 5.5" fill="none" stroke="#fff" stroke-width="1"/></svg>Merch</li>
    </ul>
  </div>

  <div class="abs foot-col" style="left:457px">
    <h3>FOLLOW US</h3>
    <ul>
      <li><span class="dot"></span>Townboard</li>
      <li><span class="dot"></span>Snapgrid</li>
      <li><span class="dot"></span>Chirper</li>
      <li><span class="dot"></span>Worklink</li>
      <li><span class="dot"></span>Viewtube</li>
    </ul>
  </div>

  <div class="abs foot-col contact" style="left:597px; top:1001px">
    <h3>CONTACT US</h3>
    <ul>
      <li><svg width="7" height="9" viewBox="0 0 7 9"><path d="M3.5 9C1.2 5.8 0 4.5 0 3.3a3.5 3.5 0 0 1 7 0C7 4.5 5.8 5.8 3.5 9z" fill="#fff"/><circle cx="3.5" cy="3.3" r="1.2" fill="#231f20"/></svg><span style="margin-left:3px">123 Lorem ipsum dolor sit amet<br>consectetur adipiscing.</span></li>
      <li><svg width="9" height="9" viewBox="0 0 9 9"><rect width="9" height="9" rx="1.5" fill="#fff"/><path d="M2.6 2c.6 2.3 2 3.7 4.3 4.4l-.4 1C3.9 6.7 2 4.8 1.6 2.4z" fill="#231f20"/></svg><span>207-555-0142</span></li>
      <li><svg width="10" height="8" viewBox="0 0 10 8"><rect width="10" height="8" rx="1" fill="#fff"/><path d="M.5 1 5 4.6 9.5 1" fill="none" stroke="#231f20" stroke-width="1"/></svg><span>beerME@kestrelhollowbrew.com.</span></li>
    </ul>
    <div class="cards"><span></span><span></span><span></span><span></span></div>
  </div>

  <div class="abs foot-rule"></div>
  <p class="abs copyright">© copyrights 2022 Kestrel Hollow Brewing Company &nbsp;|&nbsp;&nbsp;&nbsp; All rights reserved.</p>

</body>
</html>
```